New landing page

We have an existing design at www.hostcorvel.com but we are not set on that design and probably want something different.
We want to increase conversion rates and experiment with a new landing page for our brightlisting promos campains.
We want to use a more single page long design page that contains these elements on one page:

Header
Images/headline
4 offer boxes
Features
Locations (map)
Testimonials
Why HostCorvel
Footer menu

Note should also be taken of research done by Pagetrove like this:
http://pagetrove.com/landing-page-articles/the-anatomy-of-a-landing-page/

Industry/Entity Type

Brightlisting

```html
<!DOCTYPE html>
<html lang="en">
<head>
<meta charset="utf-8">
<title>HostCorvel – Your own Linux Server in 59 seconds</title>
<link rel="stylesheet" href="https://fonts.googleapis.com/css2?family=Roboto:wght@300;400;500;700&display=swap">
<style>
:root{
  --orange:#f5a40f;
  --orange-dark:#dd8f05;
  --ink:#2d2f31;
  --text:#6f7478;
  --muted:#9a9fa3;
  --line:#e4e6e8;
  --topbar:#1b1d1f;
  --nav:#2b3036;
  --panel:#34373a;
  --panel-row:#3d4043;
  --footer:#151617;
  --footer-bar:#222426;
  --white:#ffffff;
  --soft:#f6f7f8;
}
*{box-sizing:border-box;margin:0;padding:0}
html,body{width:1200px;height:3377px;overflow:hidden}
body{font-family:"Roboto",Arial,sans-serif;color:var(--text);background:var(--white);position:relative}
.wrap{position:absolute;left:173px;width:858px}
section,header,footer{position:absolute;left:0;width:1200px;overflow:hidden}
a{color:inherit;text-decoration:none}

/* top bar */
.promo-bar{top:0;height:43px;background:var(--topbar);color:#d8d8d8;font-size:12px}
.promo-bar p{position:absolute;left:173px;top:14px}
.promo-bar b{color:#fff;font-weight:500}
.promo-bar span{color:var(--orange)}
.account-btn{position:absolute;left:939px;top:7px;width:92px;height:29px;background:var(--orange);color:#fff;font-size:12px;line-height:29px;text-align:center;border-radius:2px}

/* nav */
.site-nav{top:43px;height:103px;background:var(--nav)}
.brand{position:absolute;left:173px;top:34px;display:flex;align-items:center;gap:10px;color:#fff;font-size:30px;font-weight:700;letter-spacing:-.5px}
.brand i{display:block;width:30px;height:30px;border-radius:50%;background:var(--orange)}
.nav-links{position:absolute;right:169px;top:45px;display:flex;gap:27px;list-style:none;color:#e8e8e8;font-size:12px;font-weight:500}

/* hero */
.hero{top:146px;height:525px;background:linear-gradient(180deg,#7fc6d2 0%,#b6e0e7 45%,#e9f4f6 100%)}
.hero h1{position:absolute;left:173px;top:108px;font-size:37px;font-weight:700;color:var(--ink);letter-spacing:-.5px}
.hero h2{position:absolute;left:173px;top:166px;font-size:32px;font-weight:300;color:var(--ink)}
.hero p{position:absolute;left:173px;top:216px;width:360px;font-size:11px;line-height:16px;color:#2f3b40}
.signup-btn{position:absolute;left:173px;top:322px;width:117px;height:32px;border-radius:16px;background:var(--orange);color:#fff;font-size:13px;font-weight:500;line-height:32px;padding-left:40px}
.signup-btn::before{content:"";position:absolute;left:14px;top:11px;width:10px;height:10px;border-radius:50%;background:#fff}
.hero-art{position:absolute;left:470px;top:40px;width:600px;height:440px;border-radius:6px;background:radial-gradient(ellipse at 55% 40%,#3b3e42 0%,#2a2c2f 38%,rgba(120,140,150,.35) 62%,rgba(255,255,255,0) 75%)}
.slide-arrow{position:absolute;top:260px;width:32px;height:32px;border-radius:50%;background:rgba(40,44,48,.8)}
.slide-arrow svg{position:absolute;left:9px;top:9px}
.slide-arrow.prev{left:56px}.slide-arrow.next{right:50px}
.scroll-down{position:absolute;left:580px;top:431px;width:40px;height:40px;border-radius:50%;background:rgba(60,64,68,.55)}
.scroll-down svg{position:absolute;left:12px;top:14px}
.scroll-label{position:absolute;left:557px;top:485px;font-size:14px;font-weight:700;color:#fff;letter-spacing:1px}

/* headings */
.section-title{position:absolute;left:0;width:1200px;text-align:center;color:var(--orange);font-size:24px;font-weight:500}

/* why */
.why{top:671px;height:252px;background:var(--soft)}
.why .section-title{top:24px}
.why h3{position:absolute;left:0;width:1200px;top:67px;text-align:center;font-size:14px;font-weight:400;color:#777}
.why p{position:absolute;left:203px;width:800px;text-align:center;font-size:10.5px;line-height:17px;color:var(--muted)}
.why p.first{top:110px}.why p.second{top:176px}

/* pricing */
.pricing{top:923px;height:619px;background:#fff}
.pricing .section-title{top:34px}
.plans{position:absolute;left:173px;top:106px;width:858px;height:367px;display:flex;border:1px solid var(--line)}
.plan{position:relative;width:214.5px;border-right:1px solid var(--line);text-align:center;font-size:11px;color:#555}
.plan:last-child{border-right:0}
.plan-head{height:108px;background:var(--panel);color:#fff;font-size:18px;font-weight:500;padding-top:17px}
.price{position:absolute;left:64px;top:62px;width:86px;height:86px;border-radius:50%;background:#fff;border:5px solid #e9eaeb;color:var(--orange)}
.price b{display:block;margin-top:14px;font-size:27px;font-weight:700;line-height:30px}
.price small{display:block;font-size:9px;color:#888}
.features-list{list-style:none;margin-top:55px}
.features-list li{height:36px;line-height:36px}
.features-list li:nth-child(even){background:#f3f4f5}
.plan-btn{display:block;margin:16px auto 0;width:74px;height:30px;line-height:30px;background:var(--orange);color:#fff;font-size:13px;border-radius:2px}
.plan-note{margin-top:14px;font-size:12px;color:#666}
.plan.featured{background:var(--panel);color:#eee;margin-top:-10px;height:377px;border-right:0}
.plan.featured .plan-head{padding-top:27px}
.plan.featured .price{top:72px;background:#fff}
.plan.featured .features-list li:nth-child(even){background:var(--panel-row)}
.plan.featured .plan-note{color:#fff}
.ribbon{position:absolute;left:-26px;top:22px;width:120px;height:18px;background:var(--orange);color:#3a2a00;font-size:8px;font-weight:700;line-height:18px;transform:rotate(-45deg)}

/* features */
.vps-features{top:1542px;height:383px;background:#fafafa;border-top:1px solid #eee}
.vps-features .section-title{top:30px}
.feature-grid{position:absolute;left:173px;top:83px;width:858px;display:grid;grid-template-columns:repeat(3,1fr);column-gap:10px;row-gap:26px}
.feature{position:relative;height:120px;border:1px solid #ececec;background:#fff;padding:10px 14px 0 100px}
.feature .icon{position:absolute;left:18px;top:22px;width:56px;height:56px;border-radius:50%;border:2px solid #cfd2d4;display:flex;align-items:center;justify-content:center}
.feature h4{color:var(--orange);font-size:14px;font-weight:500;margin-bottom:6px}
.feature p{font-size:11px;line-height:16px;color:var(--muted)}

/* testimonials */
.testimonials{top:1925px;height:371px;background:#fff}
.testimonials .section-title{top:26px}
.quote-box{position:absolute;left:173px;top:78px;width:858px;height:150px;border:1px solid #dadcde;box-shadow:0 1px 3px rgba(0,0,0,.06);padding:26px 30px 0 48px}
.quote-box p{font-size:10.5px;line-height:19px;color:var(--muted)}
.quote-mark{position:absolute;color:#e04a2a;font-size:34px;font-weight:700;line-height:1}
.quote-mark.open{left:16px;top:12px}.quote-mark.close{right:18px;bottom:-6px}
.author{position:absolute;left:820px;top:258px;text-align:right;font-size:11px;line-height:16px;color:#777}
.avatar{position:absolute;left:945px;top:240px;width:64px;height:64px;border-radius:50%;background:linear-gradient(160deg,#d9dadb,#aeb1b4)}

/* client benefits */
.benefits{top:2296px;height:230px;background:linear-gradient(180deg,#eef0f2 0%,#dfe3e6 60%,#e7eaec 100%)}
.benefits .section-title{top:36px}
.benefits p{position:absolute;left:203px;width:800px;top:84px;text-align:center;font-size:10.5px;line-height:16px;color:#7d8286}
.partner-row{position:absolute;left:173px;top:170px;width:858px;display:flex;justify-content:space-between;align-items:center}
.partner{height:34px;background:#c9ced2;border-radius:3px}

/* map */
.map{top:2526px;height:378px;background:linear-gradient(135deg,#ece6da 0%,#e4ddcf 50%,#ebe5d8 100%)}

/* contact */
.contact{top:2904px;height:401px;background:var(--footer);color:#c8c8c8}
.contact h2{position:absolute;left:0;width:1200px;top:38px;text-align:center;font-size:27px;font-weight:300;color:#fff}
.contact .lead{position:absolute;left:0;width:1200px;top:85px;text-align:center;font-size:13px;color:#cfcfcf}
.office{position:absolute;left:173px;top:139px;width:248px;height:232px;border:1px solid #55585b;padding:20px 18px}
.office .brand{position:static;font-size:26px}
.office .brand i{width:26px;height:26px}
.office h5{margin-top:18px;font-size:14px;font-weight:400;color:#8a8d90}
.office address{margin-top:10px;font-style:normal;font-size:11px;line-height:15px;color:#8a8d90}
.office .line{display:flex;align-items:center;gap:10px;margin-top:10px;font-size:11px;color:#8a8d90}
.link-col{position:absolute;top:150px}
.link-col h6{font-size:16px;font-weight:400;color:#fff;margin-bottom:16px}
.link-col ul{list-style:none;font-size:11px;line-height:24px;color:#b9b9b9}
.col-services{left:479px}.col-company{left:727px}.col-support{left:941px}

/* bottom bar */
.bottom-bar{top:3305px;height:72px;background:var(--footer-bar);color:#8a8c8e;font-size:10px}
.bottom-bar p{position:absolute;left:173px;top:30px}
.social{position:absolute;left:582px;top:14px;display:flex;gap:24px}
.social span{display:block;width:34px;height:34px;border-radius:50%;border:2px solid #6b6e71}
.to-top{position:absolute;left:985px;top:14px;width:42px;height:42px;border-radius:50%;background:#2f3234}
.to-top svg{position:absolute;left:14px;top:15px}
</style>
</head>
<body>

<header class="promo-bar">
  <p><b>CURRENT PROMOTION:</b> Free SSL certificate and .com domain on <span>VIP PanelDesk Managed VPS</span></p>
  <a class="account-btn" href="#">My Account</a>
</header>

<nav class="site-nav">
  <div class="brand"><i></i>HostCorvel</div>
  <ul class="nav-links">
    <li>WHY HOSTCORVEL</li><li>PRICES</li><li>FEATURES</li><li>TESTIMONIALS</li><li>LOCATIONS</li><li>CONTACT</li>
  </ul>
</nav>

<section class="hero">
  <div class="hero-art" role="img" aria-label="Illustration of a row of black server towers on a winding road against a sky and city skyline"></div>
  <h1>Your own Linux Server</h1>
  <h2>in 59 seconds</h2>
  <p>With 24x7x365 support, instant setup and upgrades, 99% uptime and our 14 day no questions asked money back guarantee, servers in New Zealand, Singapore, Hong Kong, Switzerland, Germany, South Africa and New York City... plus our great pricing, why would you look anywhere else?</p>
  <a class="signup-btn" href="#">SIGN UP</a>
  <span class="slide-arrow prev"><svg width="14" height="14" viewBox="0 0 14 14"><path d="M9 2 4 7l5 5" stroke="#fff" stroke-width="2.4" fill="none"/></svg></span>
  <span class="slide-arrow next"><svg width="14" height="14" viewBox="0 0 14 14"><path d="M5 2l5 5-5 5" stroke="#fff" stroke-width="2.4" fill="none"/></svg></span>
  <span class="scroll-down"><svg width="16" height="12" viewBox="0 0 16 12"><path d="M2 2l6 6 6-6" stroke="#fff" stroke-width="2.4" fill="none"/></svg></span>
  <span class="scroll-label">Scroll Down</span>
</section>

<section class="why">
  <h2 class="section-title">WHY HOSTCORVEL</h2>
  <h3>We're All about virtual servers and hosting</h3>
  <p class="first">Founded in 2011, HostCorvel is one of the worlds leading virtual private server hosting companies. We have grown from a single data center in Germany to provide VPS hosting services in multiple locations all over the world. Our product offering has also expanded to include higher spec'd servers as well as other addons to make hosting your valued applications and data a more enjoyable and cost-effective experience.</p>
  <p class="second">We go to great lengths to ensure we provide a great service at great prices to help your business succeed online. Being a tech company, we obviously make great use of technology ourselves to ensure our systems perform well. We have staff working in all corners of the world 24x7x365 to service your needs.</p>
</section>

<section class="pricing">
  <h2 class="section-title">PRICING TABLES</h2>
  <div class="plans">
    <div class="plan">
      <div class="plan-head">Budget VPS</div>
      <div class="price"><b>$10</b><small>per month</small></div>
      <ul class="features-list"><li>256 MB Guaranteed RAM</li><li>1x 3.4 Ghz Cores</li><li>10 GB Raid-10 Storage</li><li>300 GB Bandwidth</li><li>59 second Activation</li></ul>
      <a class="plan-btn" href="#">Sign Up</a>
      <div class="plan-note">Compare budget vps</div>
    </div>
    <div class="plan">
      <div class="plan-head">Standard VPS</div>
      <div class="price"><b>$25</b><small>per month</small></div>
      <ul class="features-list"><li>768 MB Guaranteed RAM</li><li>1x 3.4 Ghz Cores</li><li>10 GB Raid-10 Storage</li><li>300 GB Bandwidth</li><li>59 second Activation</li></ul>
      <a class="plan-btn" href="#">Sign Up</a>
      <div class="plan-note">Standard budget vps</div>
    </div>
    <div class="plan featured">
      <div class="ribbon">BEST VALUE</div>
      <div class="plan-head">Extreme</div>
      <div class="price"><b>$40</b><small>per month</small></div>
      <ul class="features-list"><li>2048 MB Guaranteed RAM</li><li>1x 3.4 Ghz Cores</li><li>10 GB Raid-10 Storage</li><li>300 GB Bandwidth</li><li>59 second Activation</li></ul>
      <a class="plan-btn" href="#">Sign Up</a>
      <div class="plan-note">Extreme budget vps</div>
    </div>
    <div class="plan">
      <div class="plan-head">Custom VPS</div>
      <div class="price"><b>$10</b><small>per month</small></div>
      <ul class="features-list"><li>Customize your RAM</li><li>1x 3.4 Ghz Cores</li><li>10 GB Raid-10 Storage</li><li>300 GB Bandwidth</li><li>59 second Activation</li></ul>
      <a class="plan-btn" href="#">Sign Up</a>
    </div>
  </div>
</section>

<section class="vps-features">
  <h2 class="section-title">VPS HOSTING FEATURES</h2>
  <div class="feature-grid">
    <div class="feature"><span class="icon"><svg width="28" height="28" viewBox="0 0 28 28"><circle cx="14" cy="14" r="11" stroke="#8a8e91" stroke-width="2.4" fill="none"/><path d="M14 7v7l5 3" stroke="#8a8e91" stroke-width="2.4" fill="none"/></svg></span><h4>59 Second Activation</h4><p>Let professionals who know the travel industries handle all yours booking requests.</p></div>
    <div class="feature"><span class="icon"><svg width="28" height="28" viewBox="0 0 28 28"><path d="M14 12v14M9 26h10" stroke="#8a8e91" stroke-width="2.4"/><circle cx="14" cy="10" r="2.5" fill="#8a8e91"/><path d="M8 4a9 9 0 0 0 0 12M20 4a9 9 0 0 1 0 12" stroke="#8a8e91" stroke-width="2" fill="none"/></svg></span><h4>99.9% Uptime</h4><p>We guarantee your VPS will have an uptime of 99.9% and strive for 100%.</p></div>
    <div class="feature"><span class="icon"><svg width="28" height="28" viewBox="0 0 28 28"><text x="14" y="22" text-anchor="middle" font-family="Roboto,Arial,sans-serif" font-size="22" font-weight="700" fill="#8a8e91">$</text></svg></span><h4>14 Day Moneyback</h4><p>If your unhappy with the service within 14 days we'll refund your money!</p></div>
    <div class="feature"><span class="icon"><svg width="28" height="28" viewBox="0 0 28 28"><path d="M14 3v12M9 10l5 5 5-5" stroke="#8a8e91" stroke-width="2.4" fill="none"/><path d="M4 16v8h20v-8" stroke="#8a8e91" stroke-width="2.4" fill="none"/></svg></span><h4>Full Root Access</h4><p>Let professionals who know the travel industries handle all yours booking requests.</p></div>
    <div class="feature"><span class="icon"><svg width="28" height="28" viewBox="0 0 28 28"><path d="M23 12a9 9 0 0 0-16-4M5 16a9 9 0 0 0 16 4" stroke="#8a8e91" stroke-width="2.4" fill="none"/><path d="M6 3v6h6M22 25v-6h-6" stroke="#8a8e91" stroke-width="2.4" fill="none"/></svg></span><h4>Global Locations</h4><p>We guarantee your VPS will have an uptime of 99.9% and strive for 100%.</p></div>
    <div class="feature"><span class="icon"><svg width="28" height="28" viewBox="0 0 28 28"><rect x="5" y="5" width="8" height="8" fill="#8a8e91"/><rect x="15" y="5" width="8" height="8" fill="#8a8e91"/><rect x="5" y="15" width="8" height="8" fill="#8a8e91"/><rect x="15" y="15" width="8" height="8" fill="#8a8e91"/></svg></span><h4>Choice of operating</h4><p>If your unhappy with the service within 14 days we'll refund your money!</p></div>
  </div>
</section>

<section class="testimonials">
  <h2 class="section-title">Testimonials</h2>
  <blockquote class="quote-box">
    <span class="quote-mark open">&#8220;</span>
    <p>Etharums ser quidem rerum facilis dolores nemis omnis fugats vitaes nemo minima rerums unsers sadips amets. Sed ut perspiciatis unde omnis iste natus error sit voluptatem accusantium doloremque laudantium, totam rem aperiam, sit voluptatem accusantium doloremque laudantium, totam rem aperiamsit. Etharums ser quidem rerum facilis dolores nemis omnis fugats vitaes nemo minima rerums unsers sadips amets. Sed ut perspiciatis unde omnis iste natus error sit voluptatem accusantium doloremque laudantium, totam rem aperiam, sit voluptatem accusantium doloremque laudantium, totam rem aperiamsit.</p>
    <span class="quote-mark close">&#8221;</span>
  </blockquote>
  <div class="author">Marco<br>Velluti</div>
  <div class="avatar" role="img" aria-label="Customer portrait photo"></div>
</section>

<section class="benefits">
  <h2 class="section-title">Client Benefits</h2>
  <p>Lorem ipsum dolor sit amet, consectetur adipisicing elit, sed do eiusmod tempor incididunt ut labore et dolore magna aliqua. Ut enim ad minim veniam, quis nostrud exercitation ullamco laboris nisi ut aliquip ex ea commodo consequat. Duis aute irure dolor in reprehenderit in voluptate velit esse cillum dolore eu fugiat nulla pariatur. Excepteur sint occaecat cupidatat non proident, sunt in culpa qui officia deserunt mollit anim id est laborum.</p>
  <div class="partner-row">
    <span class="partner" style="width:62px"></span>
    <span class="partner" style="width:78px"></span>
    <span class="partner" style="width:104px"></span>
    <span class="partner" style="width:108px"></span>
    <span class="partner" style="width:70px"></span>
    <span class="partner" style="width:90px"></span>
    <span class="partner" style="width:90px"></span>
  </div>
</section>

<section class="map" role="img" aria-label="Street map showing the office location"></section>

<footer class="contact">
  <h2>Contact us</h2>
  <p class="lead">To book an appointment with one of our Advisors, please contact one of our offices:</p>
  <div class="office">
    <div class="brand"><i></i>HostCorvel</div>
    <h5>Corporate Office</h5>
    <address>2210 Corvel Lane<br>Suite 18 Easton, MI 40021</address>
    <div class="line"><svg width="14" height="14" viewBox="0 0 14 14"><path d="M3 1h3l1 3-2 1.5a8 8 0 0 0 3.5 3.5L10 7l3 1v3c0 1-1 2-2 2A11 11 0 0 1 1 3c0-1 1-2 2-2z" fill="#8a8d90"/></svg>+65 30 555 014</div>
    <div class="line"><svg width="14" height="12" viewBox="0 0 14 12"><rect x="1" y="1" width="12" height="10" fill="none" stroke="#8a8d90" stroke-width="1.5"/><path d="M1 1l6 5 6-5" fill="none" stroke="#8a8d90" stroke-width="1.5"/></svg>sales@hostcorvel.com</div>
  </div>
  <div class="link-col col-services"><h6>Services</h6><ul><li>Budget Linux VPS</li><li>Standard Linux VPS</li><li>Extreme Linux VPS</li><li>Managed PanelDesk VPS</li><li>Custom Linux VPS</li><li>Domains and SSL certs</li></ul></div>
  <div class="link-col col-company"><h6>Company</h6><ul><li>VPS F.A.Q.</li><li>Terms of service</li><li>Acceptable Use Policy</li><li>Privacy Policy</li><li>Security</li><li>About Us</li></ul></div>
  <div class="link-col col-support"><h6>Support</h6><ul><li>Billing Login</li><li>Support Center</li><li>Knowledgebase</li><li>Contact Us</li><li>Submit a Ticket</li></ul></div>
</footer>

<footer class="bottom-bar">
  <p>© 2013 HostCorvel. All rights reserved.</p>
  <div class="social"><span></span><span></span><span></span></div>
  <span class="to-top"><svg width="14" height="10" viewBox="0 0 14 10"><path d="M2 8l5-5 5 5" stroke="#777" stroke-width="2" fill="none"/></svg></span>
</footer>

</body>
</html>
```